Business Card

Just need business logo with phone number on it. 0487 312 556
And the following on the bottom of the card.

"Your local plumbing experts".
and emblems for kelpa card, cheque and cash

```html
<!DOCTYPE html>
<html lang="en">
<head>
<meta charset="utf-8">
<title>Hillcrest Plumbing &amp; Drainage – Business Card</title>
<link rel="stylesheet" href="https://fonts.googleapis.com/css2?family=Russo+One&family=Michroma&display=swap">
<style>
  :root {
    --brand-blue: #1479bf;
    --brand-red: #e3161f;
    --card-white: #f4f4f2;
    --backdrop: #d9d4cc;
    --ink-dark: #1f2a44;
  }
  * { margin: 0; padding: 0; box-sizing: border-box; }
  html, body { width: 1200px; height: 800px; overflow: hidden; }
  body {
    background: var(--backdrop);
    display: flex; align-items: center; justify-content: center;
  }
  .business-card {
    position: relative;
    width: 900px; height: 550px;
    background: var(--card-white);
    box-shadow: 0 14px 40px rgba(0,0,0,.22);
    overflow: hidden;
  }
  .card-shapes { position: absolute; inset: 0; }
  .brand-block {
    position: absolute; left: 160px; right: 0; top: 26px;
    display: flex; flex-direction: column; align-items: center;
  }
  .brand-mark {
    font-family: "Russo One", sans-serif;
    font-size: 96px; line-height: 1;
    color: var(--brand-red);
    letter-spacing: 2px;
  }
  .brand-lockup {
    display: flex; align-items: stretch; gap: 8px;
    margin-top: 6px;
  }
  .brand-words {
    display: flex; flex-direction: column; align-items: center;
  }
  .brand-name {
    font-family: "Russo One", sans-serif;
    font-size: 66px; line-height: 1;
    color: var(--brand-red);
    letter-spacing: 3px;
  }
  .brand-trade {
    font-family: "Michroma", sans-serif;
    font-size: 20px; line-height: 1;
    color: var(--brand-blue);
    letter-spacing: 4px;
    margin-top: 8px;
    white-space: nowrap;
  }
  .brand-suffix {
    writing-mode: vertical-rl;
    font-family: "Michroma", sans-serif;
    font-size: 10px; line-height: 1;
    color: var(--brand-red);
    letter-spacing: 1px;
    white-space: nowrap;
    align-self: flex-end;
  }
  .contact-block {
    position: absolute; left: 110px; top: 372px;
  }
  .phone-number {
    font-family: "Russo One", sans-serif;
    font-size: 58px; line-height: 1;
    color: var(--brand-red);
    letter-spacing: 6px;
  }
  .tagline {
    font-family: "Michroma", sans-serif;
    font-size: 17px; line-height: 1;
    color: var(--brand-blue);
    letter-spacing: 2px;
    margin-top: 8px;
    text-transform: uppercase;
  }
  .payment-methods {
    display: flex; align-items: center; gap: 18px;
    margin: 16px 0 0 140px;
  }
  .payment-card-name {
    font-family: "Russo One", sans-serif;
    font-size: 30px; color: var(--ink-dark);
    letter-spacing: 1px;
  }
  .payment-divider { width: 2px; height: 46px; background: var(--ink-dark); }
  .payment-cash {
    font-family: "Russo One", sans-serif;
    font-size: 16px; line-height: 1.1;
    text-transform: uppercase;
  }
  .payment-cash .cheque { color: var(--brand-blue); display: block; }
  .payment-cash .cash { color: var(--brand-red); display: block; }
</style>
</head>
<body>
  <div class="business-card">
    <svg class="card-shapes" width="900" height="550" viewBox="0 0 900 550" aria-hidden="true">
      <polygon points="0,0 220,0 0,236" fill="var(--brand-blue)"/>
      <polygon points="0,240 900,340 900,362 0,262" fill="var(--brand-blue)"/>
      <polygon points="0,270 900,370 900,378 0,278" fill="var(--brand-red)"/>
      <polygon points="900,330 900,550 690,550" fill="var(--brand-red)"/>
    </svg>

    <div class="brand-block">
      <div class="brand-mark">HCPD</div>
      <div class="brand-lockup">
        <div class="brand-words">
          <div class="brand-name">HILLCREST</div>
          <div class="brand-trade">PLUMBING &amp; DRAINAGE</div>
        </div>
        <span class="brand-suffix">PTY LTD</span>
      </div>
    </div>

    <div class="contact-block">
      <div class="phone-number">0487 312 556</div>
      <div class="tagline">Your local plumbing experts</div>
      <div class="payment-methods">
        <span class="payment-card-name">KELPA</span>
        <span class="payment-divider"></span>
        <span class="payment-cash"><span class="cheque">Cheque</span><span class="cash">&amp; Cash</span></span>
      </div>
    </div>
  </div>
</body>
</html>
```